Stationary for Real Estate Investor
Holvane Estates
Stationary for Real Estate Investor - Real Estate
Creative Brief
Simple
Teodoro Vilchis
Real Estate Investor
P.O Box 417, Castro Ridge, CA 94812
teodoro@holvaneestates.example
Only use address on envelope (back flap, small print) Logo in Front Corner On letterhead only use logo (no contact info)
tvilchis27 tvilchis27
No Address on business card only on envelope.

```html
<!DOCTYPE html>
<html lang="en">
<head>
<meta charset="utf-8">
<title>Holvane Estates – Business Card</title>
<link rel="stylesheet" href="https://fonts.googleapis.com/css2?family=Open+Sans:wght@400;600;700&display=swap">
<style>
  :root {
    --backdrop: #d9d9d9;
    --card-light: #f7f7f7;
    --card-shade: #dcdcdc;
    --card-dark: #262626;
    --bar-grey: #9a9a9a;
    --ink: #1e1e1e;
    --ink-soft: #333333;
    --on-bar: #ffffff;
  }
  html, body {
    margin: 0;
    padding: 0;
    width: 1200px;
    height: 816px;
    overflow: hidden;
    background: var(--backdrop);
    font-family: "Open Sans", sans-serif;
  }
  .canvas {
    position: relative;
    width: 1200px;
    height: 816px;
  }
  .business-card {
    position: absolute;
    left: 75px;
    top: 108px;
    width: 1050px;
    height: 600px;
    border-radius: 40px;
    overflow: hidden;
    box-shadow: 0 10px 30px rgba(0,0,0,0.18);
  }
  .card-shapes {
    position: absolute;
    inset: 0;
    display: block;
  }
  .holder-name {
    position: absolute;
    left: 58px;
    top: 228px;
    margin: 0;
    font-size: 31px;
    font-weight: 600;
    color: var(--ink);
    text-transform: uppercase;
    letter-spacing: 0.5px;
  }
  .holder-title {
    position: absolute;
    left: 58px;
    top: 272px;
    margin: 0;
    font-size: 24px;
    font-weight: 400;
    color: var(--ink-soft);
  }
  .brand-name {
    position: absolute;
    right: 110px;
    top: 232px;
    margin: 0;
    font-size: 36px;
    font-weight: 400;
    color: var(--ink);
    text-transform: uppercase;
    letter-spacing: 1px;
  }
  .contact-list {
    position: absolute;
    left: 58px;
    top: 372px;
    margin: 0;
    padding: 0;
    list-style: none;
    font-size: 19px;
    color: var(--ink-soft);
    line-height: 1.25;
  }
  .contact-list li {
    display: flex;
    align-items: flex-start;
    gap: 12px;
    margin-bottom: 6px;
  }
  .contact-icon {
    flex: none;
    width: 16px;
    height: 16px;
    margin-top: 4px;
    fill: var(--ink);
  }
  .web-address {
    position: absolute;
    left: 632px;
    top: 342px;
    margin: 0;
    font-size: 26px;
    font-weight: 400;
    color: var(--on-bar);
    white-space: nowrap;
  }
</style>
</head>
<body>
<main class="canvas">
  <section class="business-card">
    <svg class="card-shapes" width="1050" height="600" viewBox="0 0 1050 600" aria-hidden="true">
      <defs>
        <linearGradient id="cardFace" x1="0" y1="0" x2="0.4" y2="1">
          <stop offset="0" stop-color="var(--card-light)"/>
          <stop offset="1" stop-color="var(--card-shade)"/>
        </linearGradient>
      </defs>
      <rect class="card-base" width="1050" height="600" fill="var(--card-dark)"/>
      <rect class="web-bar" x="580" y="326" width="520" height="66" rx="33" fill="var(--bar-grey)"/>
      <path class="card-face" d="M0 0 H1050 V318 H600 C560 318 540 340 525 375 C505 425 485 540 430 548 H0 Z" fill="url(#cardFace)"/>
    </svg>

    <h1 class="holder-name">Teodoro Vilchis</h1>
    <p class="holder-title">Real Estate Investor</p>

    <p class="brand-name">Holvane Estates</p>

    <ul class="contact-list">
      <li>
        <svg class="contact-icon" viewBox="0 0 16 16" aria-hidden="true"><path d="M1 5c0-2 3-3 7-3s7 1 7 3v1.5h-3.5V5h-7v1.5H1zM3 8l2-2h6l2 2v6H3zm5 1.5a2 2 0 1 0 0 4 2 2 0 0 0 0-4z"/></svg>
        <span>510 555 0148</span>
      </li>
      <li>
        <svg class="contact-icon" viewBox="0 0 16 16" aria-hidden="true"><path d="M3.5 1 6 3.5 4.5 5.5c1 2.2 3.3 4.5 6 6L12.5 10 15 12.5 13 15C7 14.5 1.5 9 1 3z"/></svg>
        <span>510 555 0148</span>
      </li>
      <li>
        <svg class="contact-icon" viewBox="0 0 16 16" aria-hidden="true"><path d="M1 3h14v10H1zm1.5 1.2V5l5.5 4 5.5-4v-.8L8 8.2z"/></svg>
        <span>teodoro@holvaneestates.example</span>
      </li>
    </ul>

    <p class="web-address">www.holvaneestates.example</p>
  </section>
</main>
</body>
</html>
```